Dental marketing ad poster

I recently opened a new dental practice about 2 months ago and would like to have an ad designed for an A-frame poster to place outside our office. The goal of this ad is to attract and appeal to potential patients so they feel encouraged to come into the practice.
I’m leaving the creative direction up to you—I’d like to see what you can come up with. The ad can be funny or serious, but it should be eye-catching and patient-focused. Please highlight that we provide crowns, implants and teeth whitening.
My theme color is green but I’ll accept any color
Let me see your ideas!
Dentistry

```html
<!DOCTYPE html>
<html lang="en">
<head>
<meta charset="utf-8">
<title>Willowmere Dentistry – Crowns Poster</title>
<link href="https://fonts.googleapis.com/css2?family=Archivo:wght@400;500;700;800&display=swap" rel="stylesheet">
<style>
  :root {
    --stage: #d6d6d8;
    --amber-top: #dca043;
    --amber-mid: #e9ad55;
    --amber-light: #fdc775;
    --rust: #cd782f;
    --gold-strip: #d3963f;
    --green: #1d994c;
    --green-deep: #08532a;
    --green-band: #0d6d35;
    --gold-text: #fcc774;
    --white: #ffffff;
  }
  * { margin: 0; padding: 0; box-sizing: border-box; }
  html, body {
    width: 1200px;
    height: 1200px;
    overflow: hidden;
    background: var(--stage);
    font-family: "Archivo", "Helvetica Neue", Arial, sans-serif;
  }
  .poster {
    position: absolute;
    left: 220px;
    top: 30px;
    width: 760px;
    height: 1140px;
    background: var(--green);
    overflow: hidden;
    color: var(--white);
  }
  .hero-visual {
    position: absolute;
    left: 0; top: 0;
    width: 760px;
    height: 679px;
    background:
      radial-gradient(ellipse 60% 55% at 72% 62%, #fff3d6 0%, rgba(255,236,200,0.55) 22%, rgba(253,199,117,0) 55%),
      linear-gradient(180deg, var(--amber-top) 0%, var(--amber-mid) 45%, var(--amber-light) 100%);
  }
  .headline-band {
    position: absolute;
    left: 0; top: 420px;
    width: 760px;
    height: 259px;
    background: linear-gradient(90deg, var(--rust) 0%, rgba(221,140,62,0.85) 30%, rgba(245,180,95,0.35) 60%, rgba(253,199,117,0) 85%);
  }
  .headline {
    position: absolute;
    left: 45px;
    top: 446px;
    line-height: 1;
    text-transform: uppercase;
    letter-spacing: -0.5px;
  }
  .headline .big { display: block; font-size: 62px; font-weight: 800; line-height: 0.9; }
  .headline .small { display: block; font-size: 42px; font-weight: 500; line-height: 1.05; margin: 2px 0 0; }
  .headline .big + .big { margin-top: 4px; }
  .gold-strip {
    position: absolute;
    left: 0; top: 679px;
    width: 760px; height: 19px;
    background: var(--gold-strip);
  }
  .intro-band {
    position: absolute;
    left: 0; top: 698px;
    width: 760px; height: 96px;
    background: linear-gradient(90deg, var(--green-deep) 0%, var(--green-band) 40%, var(--green) 100%);
  }
  .intro {
    position: absolute;
    left: 45px; top: 721px;
    font-size: 27px;
    line-height: 31px;
    font-weight: 400;
    letter-spacing: -0.3px;
  }
  .intro strong { font-weight: 700; }
  .services {
    position: absolute;
    left: 45px; top: 866px;
    font-size: 42px;
    font-weight: 500;
    color: var(--gold-text);
    letter-spacing: -0.8px;
    white-space: nowrap;
  }
  .services .divider { color: var(--white); margin: 0 12px; font-weight: 400; }
  .brand {
    position: absolute;
    left: 45px; top: 1058px;
    font-size: 26px;
    font-weight: 700;
    color: var(--white);
    letter-spacing: 0.2px;
  }
  .cta {
    position: absolute;
    left: 372px; top: 1047px;
    width: 392px; height: 57px;
    background: var(--green-deep);
    border: 1.5px solid var(--gold-text);
    border-right: none;
    display: flex;
    align-items: center;
    padding-left: 22px;
    font-size: 22px;
    letter-spacing: -0.6px;
    white-space: nowrap;
  }
  .cta strong { color: var(--gold-text); font-weight: 700; margin: 0 5px; }
</style>
</head>
<body>
  <main class="poster">
    <div class="hero-visual" role="img" aria-label="Glossy white molar wearing a golden crown, with a bright light sparkle, on a warm orange backdrop"></div>
    <div class="headline-band"></div>
    <h1 class="headline">
      <span class="big">Crowns</span>
      <span class="small">Fit for a</span>
      <span class="big">King</span>
      <span class="big">(or Queen)!</span>
    </h1>
    <div class="gold-strip"></div>
    <div class="intro-band"></div>
    <p class="intro">From <strong>implants</strong> to <strong>whitening</strong>, we craft smiles<br>worth showing off.</p>
    <p class="services">Crowns<span class="divider">|</span>Implants<span class="divider">|</span>Teeth whitening</p>
    <p class="brand">Willowmere Dentistry</p>
    <div class="cta">Book Your<strong>Royal Smile</strong>Today!</div>
  </main>
</body>
</html>
```